Corvale Holdings Business Cards

Hello. I need business cards designed with our new logo. I'd like to see at least 3 different designs. At least one with a dark background, and at least one with a white background. Maybe one with gray or blue for the background. Play with gradient colors and maybe even insert a pic of a skyline in the background of one or more of them. Use your judgement. We will need 2 cards printed. They need to accommodate the employee name, title, company address, phone, email, and website. Thanks.

Target Market(s)

Wealthy mature investors.

Contact Information for Business Card

Single-sided, professional, clean design that incorporates our logo.

Font styles to use
Sans Serif

Requirements
Must have
• Our new logo needs to be featured on it. (See attached.)
• Employee Name (In all CAPS)
• Title
• Street Address, City, ST Zip Code
• Cell Phone #, Email Address, Website Address
Nice to have
• Design that blends well with our new logo and its colors, or a city scape or other graphic design that looks like an apartment complex in the background. Blues and grays are nice, but use your judgement.
Should not have
• Modern or oriental looking designs or bright colors.

```html
<!DOCTYPE html>
<html lang="en">
<head>
<meta charset="utf-8">
<title>Corvale Holdings Business Cards</title>
<link rel="stylesheet" href="https://fonts.googleapis.com/css2?family=Open+Sans:ital,wght@0,400;0,600;0,700;1,400;1,700&display=swap">
<style>
  :root {
    --brand-blue: #29a3e0;
    --ink-gray: #5f6163;
    --card-gray: #6d6e70;
    --stripe-gray: #6b6c6e;
    --paper: #ffffff;
    --backdrop: #2b2b2d;
  }
  * { box-sizing: border-box; margin: 0; padding: 0; }
  html, body { width: 1200px; height: 900px; overflow: hidden; }
  body {
    background: var(--backdrop);
    font-family: "Open Sans", sans-serif;
    position: relative;
  }
  .card {
    position: absolute;
    left: 280px;
    width: 640px;
    height: 366px;
    box-shadow: 0 12px 30px rgba(0,0,0,.45);
    overflow: hidden;
  }
  .card-front { top: 56px; background: var(--paper); }
  .card-back { top: 478px; background: var(--card-gray); }

  .holder { position: absolute; left: 44px; top: 40px; }
  .holder-name {
    color: var(--brand-blue);
    font-weight: 700;
    font-style: italic;
    font-size: 25px;
    line-height: 32px;
    letter-spacing: .5px;
    text-transform: uppercase;
  }
  .holder-title {
    color: var(--ink-gray);
    font-style: italic;
    font-size: 15px;
    line-height: 22px;
  }
  .divider {
    position: absolute;
    left: 44px; right: 44px; top: 112px;
    height: 1px;
    background: var(--brand-blue);
  }
  .contact-list { position: absolute; left: 44px; top: 130px; list-style: none; }
  .contact-item {
    display: flex; align-items: center; gap: 8px;
    color: var(--ink-gray);
    font-style: italic;
    font-size: 15px;
    line-height: 24px;
  }
  .contact-icon { width: 13px; height: 13px; fill: var(--brand-blue); }

  .brand {
    position: absolute;
    display: flex; align-items: center; gap: 12px;
  }
  .card-front .brand { right: 44px; top: 36px; }
  .brand-mark { background: var(--brand-blue); flex: none; }
  .card-front .brand-mark { width: 18px; height: 18px; }
  .brand-name {
    color: var(--brand-blue);
    font-weight: 600;
    text-transform: uppercase;
    letter-spacing: 1.5px;
    line-height: 1.1;
  }
  .card-front .brand-name { font-size: 22px; }

  .address {
    position: absolute;
    right: 44px; top: 212px;
    text-align: right;
    color: var(--ink-gray);
    font-style: italic;
    font-size: 15px;
    line-height: 22px;
  }
  .footer-band { position: absolute; left: 0; bottom: 0; width: 640px; height: 110px; }
  .website {
    position: absolute;
    right: 44px; bottom: 5px;
    color: var(--paper);
    font-style: italic;
    font-size: 15px;
    line-height: 22px;
  }

  .card-back .brand {
    left: 0; right: 0; top: 0; bottom: 0;
    justify-content: center;
  }
  .card-back .brand-mark { width: 28px; height: 28px; }
  .card-back .brand-name { font-size: 38px; }
</style>
</head>
<body>
  <section class="card card-front">
    <div class="holder">
      <p class="holder-name">Daniel Reyes</p>
      <p class="holder-title">President</p>
    </div>

    <div class="brand">
      <span class="brand-mark"></span>
      <span class="brand-name">Corvale Holdings, LLC</span>
    </div>

    <div class="divider"></div>

    <ul class="contact-list">
      <li class="contact-item">
        <svg class="contact-icon" viewBox="0 0 24 24" aria-hidden="true"><path d="M6.6 10.8a15.1 15.1 0 0 0 6.6 6.6l2.2-2.2c.3-.3.7-.4 1-.2 1.1.4 2.3.6 3.6.6.6 0 1 .4 1 1V20c0 .6-.4 1-1 1A17 17 0 0 1 3 4c0-.6.4-1 1-1h3.5c.6 0 1 .4 1 1 0 1.3.2 2.5.6 3.6.1.3 0 .7-.2 1z"/></svg>
        949-555-0187
      </li>
      <li class="contact-item">
        <svg class="contact-icon" viewBox="0 0 24 24" aria-hidden="true"><path d="M2 5h20v14H2z M2 5l10 8 10-8" /></svg>
        info@corvaleholdings.com
      </li>
    </ul>

    <p class="address">1180 Harbor Crest Dr<br>Laguna Shores CA 92651</p>

    <svg class="footer-band" viewBox="0 0 640 110" aria-hidden="true">
      <path d="M0 24 L280 62 Q300 65 312 72 L0 32 Z" fill="var(--stripe-gray)"/>
      <path d="M0 40 L290 74 Q312 77 330 80 L640 80 L640 110 L0 110 Z" fill="var(--brand-blue)"/>
    </svg>
    <p class="website">corvaleholdings.com</p>
  </section>

  <section class="card card-back">
    <div class="brand">
      <span class="brand-mark"></span>
      <span class="brand-name">Corvale Holdings, LLC</span>
    </div>
  </section>
</body>
</html>
```